Brightvale Energy International Website

Brightvale Energy – Lighting the Path for
UK Households Responsibly.

New Launch Website

Focus on 4 Product Categories

- Solar PV
- Battery Energy Storage
- EV Charging
- Heat Pumps

Add

Energy News
Enquire Now button Top right every page
Contact us page

Follow Tovelin.co.uk for similar content pages

Target Market(s)

Residential home owners UK NOT US

Industry/Entity Type

Solar energy, home energy , EV charging

Coding

Coded - Design and coding required

Number of Pages Required

5+ page

Font styles to use
Sans Serif

Colors
0054AA
0677BA
7BADD7
CADEEF
E8F1F8
59FF00
82FF00
B8FF75
E3FFCB
F4FFEA
FFF300
FFF600
FEFA6F
FFFEC7
FFFEE8

Requirements
Must have
• Strong brand logo on every page, clear content bar
Nice to have
• Add these logos from TovelIn.co.uk

```html
<!DOCTYPE html>
<html lang="en">
<head>
<meta charset="utf-8">
<title>Brightvale Energy – Lighting the Path for UK Households Responsibly</title>
<link href="https://fonts.googleapis.com/css2?family=Poppins:ital,wght@0,400;0,500;0,600;0,700;1,500&display=swap" rel="stylesheet">
<style>
:root{
  --navy:#0c3a5b;
  --navy-deep:#0a2f4b;
  --green:#27a548;
  --text:#5d6670;
  --line:#d9dee3;
  --white:#ffffff;
  --sun:#f7c530;
}
*{box-sizing:border-box;margin:0;padding:0}
html,body{width:1200px;height:5338px;overflow:hidden}
body{position:relative;font-family:'Poppins',sans-serif;color:var(--navy);background:var(--white)}
.abs{position:absolute}
.center{left:0;width:1200px;text-align:center}
.section-title{font-size:37px;font-weight:600;letter-spacing:.3px;color:var(--navy)}
.section-lead{font-size:12.5px;line-height:21px;color:var(--text);width:720px;left:240px;text-align:center}
.btn{background:var(--navy);color:#fff;border-radius:22px;font-size:11.5px;font-weight:500;display:flex;align-items:center;justify-content:center}

/* hero */
.hero-photo{left:0;top:0;width:1200px;height:750px;background:linear-gradient(100deg,#1f5f93 0%,#2f79b0 38%,#6b86a0 62%,#a6593a 85%,#8c4529 100%)}
.nav{left:150px;top:42px;width:900px;height:62px;background:#fff;border-radius:31px;display:flex;align-items:center;font-size:12px;color:var(--navy);font-weight:500}
.nav a{position:absolute;color:var(--navy);text-decoration:none}
.nav .contact{right:8px;width:136px;height:46px;background:var(--navy);color:#fff;border-radius:23px;display:flex;align-items:center;justify-content:center;font-size:11.5px}
.logo-badge{left:538px;top:8px;width:124px;height:124px;border-radius:50%;background:#fff;display:flex;flex-direction:column;align-items:center;justify-content:center;line-height:24px;font-size:21px;font-weight:600;color:var(--navy)}
.hero-title{left:150px;top:160px;font-size:106px;font-weight:600;color:#fff;letter-spacing:1px}
.hero-sub{left:150px;font-size:37px;font-weight:500;color:#fff}
.tab{left:150px;width:230px;height:30px;border:1.5px solid rgba(255,255,255,.75);border-radius:9px;color:#fff;font-size:11px;display:flex;align-items:center;justify-content:space-between;padding:0 12px}
.tab-card{left:150px;top:555px;width:230px;height:90px;background:#fff;border-radius:12px;padding:12px 12px}
.tab-card h4{font-size:12px;font-weight:500;color:var(--navy)}
.tab-card p{font-size:6.5px;line-height:9px;color:var(--text);margin-top:6px;width:195px}
.tab-card a{display:block;font-size:8px;color:var(--navy);margin-top:6px;text-decoration:underline}

/* about */
.about-art{left:44px;top:838px;width:520px;height:530px;border-radius:50%;background:radial-gradient(circle at 50% 50%,#c96b3d 0%,#8aa9c6 40%,#f6cf43 62%,#ffffff 72%)}
.about-title{left:576px;top:940px;font-size:35px;font-weight:600;line-height:58px}
.about-text{left:576px;top:1062px;width:470px;font-size:12px;line-height:21px;color:var(--text)}
.check{left:576px;font-size:12px;color:var(--navy);display:flex;align-items:center;gap:10px}
.num{width:15px;height:15px;flex:0 0 15px;border-radius:50%;background:var(--green);color:#fff;font-size:8px;display:flex;align-items:center;justify-content:center}

/* services */
.service-scene{left:0;top:1783px;width:1200px;height:421px;background:linear-gradient(180deg,#eef2f5 0%,#b7c3a2 22%,#7e8d5c 40%,#2d5793 55%,#1d3f7c 80%,#3a67a8 100%)}
.service-card{width:214px;height:172px;background:#fff;border-radius:0 0 10px 10px;text-align:center;padding-top:20px}
.service-card.featured{background:var(--navy);border-radius:10px;height:185px}
.ico{width:62px;height:62px;border-radius:50%;background:var(--green);margin:0 auto;display:flex;align-items:center;justify-content:center}
.service-card h3{font-size:14px;font-weight:500;color:var(--navy);margin-top:16px}
.service-card p{font-size:11.5px;line-height:20px;color:var(--text);margin:10px auto 0;width:185px}
.service-card.featured h3,.service-card.featured p{color:#fff}

/* benefits */
.benefit-art{left:530px;top:2425px;width:262px;height:467px;border-radius:40px;background:radial-gradient(ellipse at 50% 30%,#f7cf3f 0%,#f6d66a 22%,#5f88c4 48%,#2c4f8e 70%,#dfe7f1 100%)}
.benefit{left:150px;display:flex;gap:12px;z-index:2}
.benefit h4{font-size:15px;font-weight:500;color:var(--navy)}
.benefit p{font-size:12px;color:var(--text);margin-top:6px;white-space:nowrap}
.benefit-note{left:804px;top:2716px;width:250px;font-size:12px;line-height:21px;color:var(--text);z-index:2}

/* blog */
.post{top:3147px;width:291px;height:321px;border:1px solid var(--line);border-radius:6px;background:#fff;padding:8px}
.post .thumb{height:197px;background:linear-gradient(180deg,#8fb5d8 0%,#3e5f9c 55%,#c56a44 100%)}
.post h3{font-size:14px;font-weight:500;margin:14px 0 0 4px;color:var(--navy)}
.post p{font-size:11.5px;line-height:20px;color:var(--text);margin:8px 0 0 4px}
.post a{display:block;text-align:center;font-size:11.5px;font-weight:500;color:var(--navy);margin-top:8px;text-decoration:none}

/* contact */
.contact-ico{width:44px;height:44px;border-radius:50%;background:var(--green);display:flex;align-items:center;justify-content:center}
.contact-info{font-size:10px;line-height:15px;color:var(--text);text-align:center;width:240px}
.contact-scene{left:0;top:3880px;width:1200px;height:484px;background:linear-gradient(180deg,#ffffff 0%,#e3ecf2 18%,#9bb36b 42%,#6f8a45 55%,#2c5797 70%,#1a3b78 100%)}
.field{background:#fff;border:1px solid var(--line);border-radius:8px;font-size:11.5px;color:#7a838c;padding:12px 18px}
.submit{left:213px;top:4134px;width:774px;height:31px;border-radius:16px;background:var(--navy);color:#fff;font-size:11.5px;font-weight:500;display:flex;align-items:center;justify-content:center}

/* testimonials */
.review{top:4614px;width:290px;height:243px;border:1.5px solid #b8c2cb;border-radius:12px;background:#fff;padding:20px 16px}
.review.dark{background:var(--navy);border-color:var(--navy)}
.quote{font-size:92px;font-weight:700;line-height:70px;color:var(--green);height:44px;overflow:hidden}
.review p{font-size:9.5px;line-height:18px;color:var(--navy);margin-top:20px}
.review.dark p,.review.dark .who h4,.review.dark .who span{color:#fff}
.review hr{border:0;border-top:1.5px solid #b8c2cb;margin:20px -16px 0}
.who{display:flex;align-items:center;gap:12px;margin-top:14px}
.avatar{width:36px;height:36px;border-radius:50%;background:#c8b8a6}
.who h4{font-size:13px;font-weight:500;font-style:italic;color:var(--navy)}
.who span{font-size:9.5px;font-style:italic;color:var(--navy)}

/* footer */
.footer{left:0;top:4954px;width:1200px;height:384px;background:linear-gradient(180deg,#0f4a7a 0%,#1a64a0 55%,#2c7dbf 100%);color:#fff}
.footer-logo{left:156px;top:67px;width:136px;height:136px;border-radius:50%;background:#fff;display:flex;flex-direction:column;align-items:center;justify-content:center;font-size:21px;font-weight:600;line-height:25px;color:var(--navy)}
.footer h5{font-size:13px;font-weight:500}
.footer ul{list-style:none;font-size:11px;line-height:26px;color:#e3ecf4}
.footer .small{font-size:9px;color:#e3ecf4}
</style>
</head>
<body>

<!-- HERO -->
<header>
  <div class="abs hero-photo" role="img" aria-label="Photo of a brick house roof fitted with solar panels under a blue sky"></div>
  <nav class="abs nav">
    <a style="left:26px">Home</a>
    <a style="left:130px">About us</a>
    <a style="left:252px">Services</a>
    <a style="left:566px">Benefits</a>
    <a style="left:683px">Blog</a>
    <a class="contact">Contact Us</a>
  </nav>
  <div class="abs logo-badge"><span>Brightvale</span><span>Energy</span></div>
  <h1 class="abs hero-title">POWERING</h1>
  <p class="abs hero-sub" style="top:296px">THE FUTURE OF UK HOMES</p>
  <p class="abs hero-sub" style="top:362px">SUSTAINABLY</p>
  <div class="abs tab" style="top:455px"><span>Solar PV</span><span>→</span></div>
  <div class="abs tab" style="top:490px"><span>Battery Energy Storage</span><span>→</span></div>
  <div class="abs tab" style="top:523px"><span>EV Charging</span><span>→</span></div>
  <div class="abs tab-card">
    <h4>Heat Pumps</h4>
    <p>Efficient, low-carbon heating that keeps every room warm and comfortable through the colder months</p>
    <a>See More</a>
  </div>
</header>

<!-- ABOUT -->
<section>
  <div class="abs about-art" role="img" aria-label="Illustration of a sun framing a house roof with solar panels"></div>
  <h2 class="abs about-title">BUILDING A SUSTAINABLE<br>TOMORROW, TODAY</h2>
  <div class="abs about-text">
    <p>Brightvale Energy is dedicated to transforming the way UK homes use energy. By combining solar power, battery storage, EV charging, and heat pumps, we deliver smart solutions that cut costs and</p>
    <p style="margin-top:14px">make homes more sustainable. Our mission is simple: affordable, reliable, and eco-friendly energy for every household</p>
  </div>
  <div class="abs check" style="top:1208px"><span class="num">1</span>Company ka main kaam (solar + clean energy solutions for UK homes)</div>
  <div class="abs check" style="top:1241px"><span class="num">2</span>Mission (reduce bills + eco-friendly future)</div>
  <div class="abs check" style="top:1274px"><span class="num">3</span>Focus on UK market</div>
  <div class="abs btn" style="left:576px;top:1316px;width:133px;height:44px">Learn More</div>
</section>

<!-- SERVICES -->
<section>
  <h2 class="abs center section-title" style="top:1488px">FROM SUNLIGHT TO POWER ALL IN ONE PLACE</h2>
  <p class="abs section-lead" style="top:1549px">Brightvale Energy is dedicated to transforming the way UK homes use energy. By combining solar power, battery storage, EV charging.</p>
  <div class="abs btn" style="left:535px;top:1613px;width:130px;height:43px">Learn More</div>
  <div class="abs service-scene" role="img" aria-label="Photo of rolling countryside above rows of solar panels"></div>

  <div class="abs service-card" style="left:150px;top:1793px">
    <div class="ico"><svg width="34" height="22" viewBox="0 0 34 22"><rect x="1" y="1" width="28" height="20" rx="3" fill="none" stroke="#fff" stroke-width="2.5"/><rect x="30" y="7" width="3" height="8" fill="#fff"/><path d="M17 4 L11 12 H16 L13 18 L20 9 H15 Z" fill="#fff"/></svg></div>
    <h3>Battery Energy Storage</h3>
    <p>Brightvale is dedicated to transforming the way</p>
  </div>
  <div class="abs service-card" style="left:379px;top:1793px">
    <div class="ico"><svg width="24" height="32" viewBox="0 0 24 32"><rect x="2" y="2" width="16" height="26" rx="3" fill="none" stroke="#fff" stroke-width="2.5"/><path d="M11 7 L6 16 H10 L8 23 L14 13 H10 Z" fill="#fff"/><path d="M18 12 H22 V20" fill="none" stroke="#fff" stroke-width="2"/></svg></div>
    <h3>EV Charging Solutions</h3>
    <p>Brightvale is dedicated to transforming the way</p>
  </div>
  <div class="abs service-card featured" style="left:607px;top:1708px">
    <div class="ico"><svg width="30" height="30" viewBox="0 0 30 30"><circle cx="8" cy="8" r="4" fill="#fff"/><g stroke="#fff" stroke-width="2"><line x1="8" y1="0" x2="8" y2="2"/><line x1="0" y1="8" x2="2" y2="8"/><line x1="2" y1="2" x2="4" y2="4"/></g><rect x="12" y="12" width="16" height="12" fill="none" stroke="#fff" stroke-width="2"/><line x1="20" y1="12" x2="20" y2="24" stroke="#fff" stroke-width="1.5"/><line x1="12" y1="18" x2="28" y2="18" stroke="#fff" stroke-width="1.5"/><line x1="20" y1="24" x2="20" y2="29" stroke="#fff" stroke-width="2"/></svg></div>
    <h3>Solar PV Systems</h3>
    <p>Brightvale is dedicated to transforming the way</p>
  </div>
  <div class="abs service-card" style="left:837px;top:1793px">
    <div class="ico"><svg width="32" height="28" viewBox="0 0 32 28"><rect x="2" y="6" width="22" height="20" rx="2" fill="none" stroke="#fff" stroke-width="2.5"/><circle cx="13" cy="16" r="5" fill="none" stroke="#fff" stroke-width="2"/><path d="M24 10 H30 M24 16 H30" stroke="#fff" stroke-width="2"/><path d="M6 2 Q9 0 12 2" fill="none" stroke="#fff" stroke-width="2"/></svg></div>
    <h3>Heat Pumps</h3>
    <p>Brightvale is dedicated to transforming the way</p>
  </div>
</section>

<!-- BENEFITS -->
<section>
  <h2 class="abs center section-title" style="top:2303px">BENEFITS THAT GO BEYOND ENERGY SAVINGS</h2>
  <p class="abs section-lead" style="top:2363px">Brightvale Energy is dedicated to transforming the way UK homes use energy. By combining solar power, battery storage, EV charging.</p>
  <div class="abs benefit-art" role="img" aria-label="Illustration of a tilted solar panel in front of a bright sun"></div>
  <div class="abs benefit" style="top:2522px"><span class="num">1</span><div><h4>Energy Bill Savings</h4><p>Company ka main kaam (solar + clean energy solution</p></div></div>
  <div class="abs benefit" style="top:2595px"><span class="num">2</span><div><h4>Energy Independence</h4><p>Company ka main kaam (solar + clean energy</p></div></div>
  <div class="abs benefit" style="top:2668px"><span class="num">3</span><div><h4>Eco-Friendly Living</h4><p>Company solar + clean energy solution</p></div></div>
  <div class="abs benefit" style="top:2740px"><span class="num">4</span><div><h4>Increased Home Value</h4><p>Companyclean energy solution</p></div></div>
  <div class="abs benefit" style="top:2812px"><span class="num">5</span><div><h4>Reliable Power</h4><p>Company ka main</p></div></div>
  <p class="abs benefit-note">Brightvale Energy is dedicat transforming the way UK homes use ene. combining solar power, battery</p>
  <div class="abs btn" style="left:804px;top:2798px;width:133px;height:44px">Discover More</div>
</section>

<!-- BLOG -->
<section>
  <h2 class="abs center section-title" style="top:2999px">YOUR SOURCE FOR CLEAN ENERGY KNOWLEDGE</h2>
  <p class="abs section-lead" style="top:3059px">Brightvale Energy is dedicated to transforming the way UK homes use energy. By combining solar power, battery storage, EV charging.</p>
  <article class="abs post" style="left:150px">
    <div class="thumb" role="img" aria-label="Photo of a white house with a solar panel roof"></div>
    <h3>Journey To A Sustainable Future</h3>
    <p>Lorem ipsum dolor sit amet consectetur. Quis suspendisse a egestas consequat.</p>
    <a>Read More »</a>
  </article>
  <article class="abs post" style="left:454px">
    <div class="thumb" role="img" aria-label="Photo of rows of solar panels on a roof under blue sky"></div>
    <h3>Eco Innovations: Trends And Tips</h3>
    <p>Lorem ipsum dolor sit amet consectetur. Quis suspendisse a egestas consequat.</p>
    <a>Read More »</a>
  </article>
  <article class="abs post" style="left:761px">
    <div class="thumb" role="img" aria-label="Photo of a tiled roof fitted with solar panels"></div>
    <h3>Eco Enthusiast: Green Living Tips</h3>
    <p>Lorem ipsum dolor sit amet consectetur. Quis suspendisse a egestas consequat.</p>
    <a>Read More »</a>
  </article>
</section>

<!-- CONTACT -->
<section>
  <h2 class="abs center section-title" style="top:3568px">CONNECT WITH OUR ENERGY EXPERTS</h2>
  <p class="abs section-lead" style="top:3630px">Brightvale Energy is dedicated to transforming the way UK homes use energy. By combining solar power, battery storage, EV charging.</p>
  <div class="abs contact-ico" style="left:239px;top:3705px"><svg width="22" height="22" viewBox="0 0 24 24"><path d="M6.6 10.8a15 15 0 0 0 6.6 6.6l2.2-2.2a1 1 0 0 1 1-.25 11 11 0 0 0 3.6.6 1 1 0 0 1 1 1V20a1 1 0 0 1-1 1A17 17 0 0 1 3 4a1 1 0 0 1 1-1h3.5a1 1 0 0 1 1 1 11 11 0 0 0 .6 3.6 1 1 0 0 1-.25 1z" fill="#fff"/></svg></div>
  <div class="abs contact-ico" style="left:561px;top:3705px"><svg width="22" height="22" viewBox="0 0 24 24"><path d="M12 2a7 7 0 0 0-7 7c0 5 7 13 7 13s7-8 7-13a7 7 0 0 0-7-7z" fill="none" stroke="#fff" stroke-width="2.2"/><circle cx="12" cy="9" r="2.6" fill="#fff"/></svg></div>
  <div class="abs contact-ico" style="left:898px;top:3705px"><svg width="24" height="20" viewBox="0 0 24 20"><rect x="2" y="2" width="20" height="16" rx="2" fill="none" stroke="#fff" stroke-width="2.2"/><path d="M2 3 L12 11 L22 3" fill="none" stroke="#fff" stroke-width="2.2"/></svg></div>
  <p class="abs contact-info" style="left:141px;top:3756px">(020) 555-0147<br>(020) 555-0198</p>
  <p class="abs contact-info" style="left:463px;top:3756px">14 Meadow Lane, Harrowfield<br>HF2 7QL</p>
  <p class="abs contact-info" style="left:800px;top:3756px">hello@brightvale-<br>mail.com</p>
  <div class="abs contact-scene" role="img" aria-label="Photo of green countryside and a village behind solar panels"></div>
  <div class="abs field" style="left:213px;top:3881px;width:378px;height:46px">First Name</div>
  <div class="abs field" style="left:607px;top:3881px;width:380px;height:46px">Last Name</div>
  <div class="abs field" style="left:213px;top:3941px;width:378px;height:46px">Phone Number</div>
  <div class="abs field" style="left:607px;top:3941px;width:380px;height:46px">Email</div>
  <div class="abs field" style="left:213px;top:4001px;width:774px;height:108px">Messages</div>
  <div class="abs submit">Submit</div>
</section>

<!-- TESTIMONIALS -->
<section>
  <h2 class="abs center section-title" style="top:4463px">TRUSTED BY HOMEOWNERS ACROSS THE UK</h2>
  <p class="abs section-lead" style="top:4524px">Brightvale Energy is dedicated to transforming the way UK homes use energy. By combining solar power, battery storage, EV charging.</p>
  <div class="abs review" style="left:150px">
    <div class="quote">“</div>
    <p>From Wholesale Orders For Busine Custom Designs For Individual Shoppers, Browse Our Full Range Of ProductWhether</p>
    <hr>
    <div class="who"><div class="avatar" role="img" aria-label="Customer portrait"></div><div><h4>Callum Reedly</h4><span>Global Directives Architect</span></div></div>
  </div>
  <div class="abs review dark" style="left:456px">
    <div class="quote">“</div>
    <p>From Wholesale Orders For Busine Custom Designs For Individual Shoppers, Browse Our Full Range Of ProductWhether</p>
    <hr>
    <div class="who"><div class="avatar" role="img" aria-label="Customer portrait"></div><div><h4>Callum Reedly</h4><span>Global Directives Architect</span></div></div>
  </div>
  <div class="abs review" style="left:761px">
    <div class="quote">“</div>
    <p>From Wholesale Orders For Busine Custom Designs For Individual Shoppers, Browse Our Full Range Of ProductWhether</p>
    <hr>
    <div class="who"><div class="avatar" role="img" aria-label="Customer portrait"></div><div><h4>Callum Reedly</h4><span>Global Directives Architect</span></div></div>
  </div>
</section>

<!-- FOOTER -->
<footer class="abs footer">
  <div class="abs footer-logo"><span>Brightvale</span><span>Energy</span></div>
  <p class="abs small" style="left:150px;top:230px">Bringing You Peace Of Mind, One Wipe At A Time Your Hygiene, Our Promise From Our Purse</p>
  <p class="abs" style="left:150px;top:276px;font-size:11px">Enter You Email</p>
  <div class="abs" style="left:150px;top:300px;width:265px;border-top:1px solid #fff"></div>
  <div class="abs" style="left:458px;top:268px;width:118px;height:37px;background:#fff;color:var(--navy);border-radius:19px;font-size:11px;font-weight:500;display:flex;align-items:center;justify-content:center">Subcribe</div>
  <h5 class="abs" style="left:719px;top:112px">Customer Care</h5>
  <ul class="abs" style="left:719px;top:150px">
    <li>My Account</li><li>Discount</li><li>Returns</li><li>Orders History</li><li>Order Tracking</li>
  </ul>
  <h5 class="abs" style="left:889px;top:112px">Contact Us</h5>
  <ul class="abs" style="left:889px;top:150px;width:190px">
    <li>info@brightvale-mail.com</li><li>+(000)-0000-000</li><li style="line-height:17px;margin-top:5px">Lorem Ipsum Dolor Sit Amet Velit Nam.</li>
  </ul>
  <div class="abs" style="left:150px;top:330px;width:900px;border-top:1px solid rgba(255,255,255,.35)"></div>
  <p class="abs small" style="left:150px;top:347px">Copyright © 2025 Brightvale Energy - All Right Reserved</p>
  <p class="abs small" style="left:856px;top:347px">Terms Of Service</p>
  <p class="abs small" style="left:978px;top:347px">Privacy Policy</p>
</footer>

</body>
</html>
```